New business card for civil engineering company - "Keystone Audit"

We need a business card designed for our new structural engineering company.

The company name is "Keystone Audit" logo files attached.

We would like the following:
* Two-sided card
* Simple design

Information to be placed on the card:
Name - Marcus Dellow
Job Title - Director / Structural Engineer
Credentials - BEng(Hons), CPEng, CMengNZ, IntPE(NZ)
Email - marcus.dellow@keystoneaudit.co.nz
mobile - 0219364058
website - www.keystoneaudit.co.nz

```html
<!DOCTYPE html>
<html lang="en">
<head>
<meta charset="UTF-8">
<title>Keystone Audit – Business Card</title>
<link href="https://fonts.googleapis.com/css2?family=Exo+2:wght@400;600;800&display=swap" rel="stylesheet">
<style>
  :root {
    --stage: #e9e9ea;
    --ink-black: #030303;
    --paper: #f4f5f6;
    --brand-blue: #2f7fc1;
    --brand-deep: #1f5f9a;
    --text-grey: #5d6066;
    --light-grey: #8a8d92;
    --rule: #3c86c6;
  }
  * { margin: 0; padding: 0; box-sizing: border-box; }
  html, body { width: 1200px; height: 600px; overflow: hidden; }
  body {
    background: var(--stage);
    font-family: "Exo 2", sans-serif;
    position: relative;
  }
  .card {
    position: absolute;
    top: 150px;
    width: 540px;
    height: 300px;
    box-shadow: 0 8px 24px rgba(0,0,0,0.18);
    overflow: hidden;
  }
  .card--front { left: 40px; background: var(--ink-black); }
  .card--back {
    left: 620px;
    background: radial-gradient(circle at 30% 35%, #ffffff 0%, var(--paper) 55%, #e6e8ea 100%);
  }

  /* Front */
  .front-brand {
    position: absolute;
    top: 112px; left: 0; right: 0;
    text-align: center;
  }
  .brand-name {
    font-weight: 600;
    color: var(--brand-blue);
    letter-spacing: 2px;
    text-transform: uppercase;
  }
  .front-brand .brand-name { font-size: 34px; }
  .brand-tagline {
    font-weight: 400;
    color: var(--brand-deep);
    letter-spacing: 3px;
    text-transform: uppercase;
  }
  .front-brand .brand-tagline { font-size: 10px; margin-top: 6px; }
  .front-web {
    position: absolute;
    bottom: 28px; left: 0; right: 0;
    text-align: center;
    color: var(--brand-deep);
    font-size: 13px;
    letter-spacing: 6px;
  }

  /* Back */
  .back-brand {
    position: absolute;
    top: 104px; right: 34px;
    text-align: right;
  }
  .back-brand .brand-name { font-size: 26px; color: var(--brand-blue); }
  .back-brand .brand-tagline { font-size: 8px; color: var(--light-grey); margin-top: 4px; }
  .rule {
    position: absolute;
    left: 30px; right: 30px;
    height: 1px;
    background: var(--rule);
  }
  .rule--top { top: 168px; left: 250px; }
  .rule--bottom { top: 240px; }
  .person {
    position: absolute;
    left: 30px; top: 180px;
  }
  .person-name {
    font-weight: 800;
    font-size: 20px;
    color: var(--brand-deep);
    letter-spacing: 1.5px;
  }
  .person-title { font-size: 11px; color: var(--text-grey); letter-spacing: 0.6px; margin-top: 2px; }
  .person-creds { font-size: 8px; color: var(--light-grey); letter-spacing: 0.5px; margin-top: 2px; }
  .contacts {
    position: absolute;
    left: 30px; right: 30px; top: 252px;
    display: flex;
    justify-content: space-between;
    font-size: 10.5px;
    color: var(--text-grey);
    letter-spacing: 0.4px;
  }
  .contact { display: flex; align-items: center; gap: 5px; }
  .contact svg { width: 12px; height: 12px; flex: none; }
</style>
</head>
<body>

<section class="card card--front" aria-label="Card front">
  <div class="front-brand">
    <div class="brand-name">Keystone Audit</div>
    <div class="brand-tagline">Peer Review Specialists</div>
  </div>
  <div class="front-web">www.keystoneaudit.co.nz</div>
</section>

<section class="card card--back" aria-label="Card back">
  <div class="back-brand">
    <div class="brand-name">Keystone Audit</div>
    <div class="brand-tagline">Peer Review Specialists</div>
  </div>
  <div class="rule rule--top"></div>

  <div class="person">
    <div class="person-name">Marcus Dellow</div>
    <div class="person-title">Director / Structural Engineer</div>
    <div class="person-creds">BEng(Hons), CPEng, CMengNZ, IntPE(NZ)</div>
  </div>
  <div class="rule rule--bottom"></div>

  <div class="contacts">
    <div class="contact">
      <svg viewBox="0 0 12 12" aria-hidden="true"><circle cx="6" cy="6" r="6" fill="#1f5f9a"/><path d="M4 3.2 5 3l.6 1.5-.7.5a4 4 0 0 0 1.9 1.9l.5-.7L9 6.8 8.8 7.8c-2.8.2-5.1-2.1-4.8-4.6Z" fill="#fff"/></svg>
      <span>0219364058</span>
    </div>
    <div class="contact">
      <svg viewBox="0 0 12 12" aria-hidden="true"><circle cx="6" cy="6" r="6" fill="#1f5f9a"/><rect x="3" y="4" width="6" height="4" fill="none" stroke="#fff" stroke-width=".8"/><path d="M3 4l3 2.2L9 4" fill="none" stroke="#fff" stroke-width=".8"/></svg>
      <span>marcus.dellow@keystoneaudit.co.nz</span>
    </div>
    <div class="contact">
      <svg viewBox="0 0 12 12" aria-hidden="true"><circle cx="6" cy="6" r="6" fill="#1f5f9a"/><circle cx="6" cy="6" r="3.3" fill="none" stroke="#fff" stroke-width=".7"/><ellipse cx="6" cy="6" rx="1.4" ry="3.3" fill="none" stroke="#fff" stroke-width=".7"/><path d="M2.7 6h6.6" stroke="#fff" stroke-width=".7"/></svg>
      <span>www.keystoneaudit.co.nz</span>
    </div>
  </div>
</section>

</body>
</html>
```